Foot and ankle surgeon requires a website design

I need a website where prospective and established patients can obtain information and then direct them to making appointments. My practice is a highly professional surgical practice specialising in surgery to the foot and ankle. My title is Mr Colin Dwyer, Podiatric Foot & Ankle Surgeon. My qualifications are: BSc MSc FACPS
The practice website will require information on: Locations, phone numbers to make appointments, general background on podiatric surgery,
I would like to include information on: my hospital appointments, surgical fellowships held, training programs undertaken, association memberships, publications written, links to useful websites
A page dedicated to common foot conditions would be useful and also a page with referral information including an online registration section that will be sent direct to the receptionist.
Examples of similar websites include:
http://www.trevorkeplinfeet.com.au/
http://www.vollardfootsurgeon.com.au/
I will provide files on logo, self photos and my personal training history etc.
Also if there is going to be a background theme I personally am associated with surfing and beach activities, it would be great if this was able to be reflected in the design.
Thank you.

```html
<!DOCTYPE html>
<html lang="en">
<head>
<meta charset="utf-8">
<title>Mr Colin Dwyer – Podiatric Foot &amp; Ankle Surgeon</title>
<link href="https://fonts.googleapis.com/css2?family=Open+Sans:wght@400;600&family=Fjalla+One&display=swap" rel="stylesheet">
<style>
:root{
  --orange:#e8820f;
  --navy:#0d3f78;
  --blue-link:#2b6fb3;
  --text:#555;
  --muted:#9a9a9a;
  --line:#e6e6e6;
  --footer:#24262b;
  --footer-deep:#1b1d21;
  --footer-text:#9ea2a8;
}
*{margin:0;padding:0;box-sizing:border-box}
html,body{width:782px;height:1200px;overflow:hidden}
body{position:relative;font-family:"Open Sans",sans-serif;color:var(--text);
  background:linear-gradient(#f6f7f9 0,#fff 130px,#fff 100%)}
.abs{position:absolute}
/* header */
.brand{left:112px;top:22px;display:flex;align-items:center;gap:8px}
.brand-dot{width:22px;height:22px;border-radius:50%;background:var(--orange)}
.brand-name{font-size:11px;font-weight:600;color:var(--navy);line-height:1.2}
.brand-sub{font-size:6px;color:var(--orange)}
.social{top:22px;width:16px;height:16px;border-radius:50%;border:1px solid #d8d8d8;background:#fff}
.call{left:568px;top:51px;font-size:10px;color:#777;display:flex;gap:5px;align-items:center}
/* nav */
.nav{left:112px;top:85px;width:558px;height:32px;background:var(--orange);display:flex;align-items:center}
.nav a{font-size:8px;color:#fff;text-decoration:none;position:absolute;top:12px}
.nav .home{position:absolute;left:0;top:0;width:50px;height:32px;background:var(--navy);display:flex;align-items:center;justify-content:center;font-size:8px;color:#fff}
/* hero */
.hero{left:112px;top:117px;width:558px;height:256px;background:linear-gradient(100deg,#f3cfc0 0%,#f0d8ce 45%,#ebe5e4 100%)}
.hero-panel{left:410px;top:164px;width:234px;height:145px;border-radius:42px;background:rgba(150,150,155,.62);text-align:center;color:#fff}
.hero-title{font-family:"Fjalla One",sans-serif;font-size:28px;margin-top:18px;letter-spacing:.3px}
.hero-text{font-size:7px;line-height:13.5px;margin:6px 22px 0}
.btn-navy{display:inline-block;margin-top:10px;background:var(--navy);color:#fff;font-size:7.5px;padding:6px 10px;border-radius:12px}
.dots{left:509px;top:326px;display:flex;gap:3px}
.dots span{width:7px;height:7px;border-radius:50%;background:#fff;border:1px solid #ccc}
.dots span.on{background:#0d5a7a;border-color:#0d5a7a}
/* welcome */
.member{left:112px;top:392px;width:173px;height:114px;border:1px solid var(--line);background:#fafafa}
.member-photo{left:0;top:0;width:98px;height:112px;background:linear-gradient(#eef1f4,#dfe5ec)}
.member-title{left:88px;top:30px;font-size:19px;color:#666;font-weight:400}
.member-sub{left:113px;top:56px;font-size:9px;letter-spacing:5px;color:#777}
.member-cta{left:113px;top:77px;font-size:10px;color:var(--orange)}
.welcome-h{left:301px;top:386px;font-size:14px;color:#444;font-weight:600}
.welcome-p{left:301px;top:410px;width:371px;font-size:6.6px;line-height:13.4px;color:var(--muted);text-align:justify}
.link{font-size:7.5px;color:var(--orange)}
/* cards */
.card{top:530px;width:177px;height:174px;border:1px solid var(--line);background:#fbfbfb}
.card-img{width:175px;height:113px}
.card h3{font-size:10.5px;font-weight:400;color:#666;margin:9px 0 0 9px}
.card p{font-size:6.6px;line-height:12.6px;color:var(--muted);margin:5px 30px 0 9px}
.card .arrow{position:absolute;right:10px;top:146px;width:12px;height:12px;border-radius:50%;border:1px solid #ccc}
/* updates */
.updates-h{left:112px;top:724px;font-size:12.5px;color:#666}
.updates-line{left:112px;top:750px;width:388px;height:1px;background:var(--line)}
.upd-img{left:113px;width:109px;height:85px}
.upd-title{left:237px;font-size:10px;color:#777}
.upd-text{left:237px;width:263px;font-size:6.6px;line-height:13.4px;color:var(--muted);text-align:justify}
.upd-more{left:237px;font-size:7.5px;color:var(--blue-link)}
/* appointment */
.appt{left:520px;top:723px;width:150px;height:225px;background:#f7f7f7;border:1px solid #eee}
.appt h2{position:absolute;left:0;width:100%;top:7px;text-align:center;font-size:14px;font-weight:400;color:var(--orange)}
.field{left:528px;width:133px;border:1px solid #e3e3e3;background:#fff;font-size:6.5px;color:#aaa;padding:8px 10px}
.btn-orange{left:562px;top:916px;width:65px;height:20px;background:var(--orange);color:#fff;font-size:7.5px;text-align:center;line-height:20px;border-radius:2px}
/* footer */
.footer{left:0;top:970px;width:782px;height:178px;background:var(--footer)}
.footer-bar{left:0;top:1148px;width:782px;height:52px;background:var(--footer-deep)}
.f-h{font-size:10.5px;color:#e8e8e8}
.f-label{font-size:7.5px;color:var(--footer-text)}
.f-text{font-size:7px;line-height:13.6px;color:var(--footer-text)}
.map{left:382px;top:1010px;width:288px;height:122px;background:linear-gradient(135deg,#dfe6cf,#ece6d3 50%,#d9e2e6)}
.f-brand{left:112px;top:1160px;display:flex;align-items:center;gap:6px;opacity:.35}
.f-brand span{font-size:9px;color:#fff;font-weight:600}
.copy{left:518px;top:1168px;font-size:7px;color:#8a8d92}
</style>
</head>
<body>

<header>
  <div class="abs brand"><div class="brand-dot"></div>
    <div><div class="brand-name">Mr Colin Dwyer</div><div class="brand-sub">Podiatric Foot &amp; Ankle Surgeon</div></div>
  </div>
  <div class="abs social" style="left:587px"></div>
  <div class="abs social" style="left:609px"></div>
  <div class="abs social" style="left:631px"></div>
  <svg class="abs" style="left:653px;top:22px" width="16" height="16" viewBox="0 0 16 16"><circle cx="8" cy="8" r="7.5" fill="#fff" stroke="#d8d8d8"/><circle cx="7.3" cy="7.3" r="3" fill="none" stroke="#444" stroke-width="1.2"/><line x1="9.5" y1="9.5" x2="11.5" y2="11.5" stroke="#444" stroke-width="1.3"/></svg>
  <div class="abs call"><svg width="10" height="9" viewBox="0 0 10 9"><path d="M1 3 Q5 0 9 3 L8 4 L6.5 3 L3.5 3 L2 4Z M3 4h4l1.5 4h-7z" fill="var(--navy)"/></svg>Call : 08 9412 7730</div>
</header>

<nav class="abs nav">
  <span class="home">HOME</span>
  <a style="left:62px">Appointments</a>
  <a style="left:141px">Surgical Fellowships</a>
  <a style="left:241px">Training programs</a>
  <a style="left:334px">Memberships</a>
  <a style="left:410px">Publications</a>
  <a style="left:481px">Contact Us</a>
</nav>

<section class="abs hero" role="img" aria-label="Photo of a bare foot wearing a black bunion correction splint on a white sheet"></section>
<div class="abs hero-panel">
  <div class="hero-title">Podiatric Surgery</div>
  <div class="hero-text">Lorem ipsum dolor sit amet, conse ctetur adipiscing elit, sed do eius mod tempor incididunt ut labore et dolore magna aliqua. Quisque bibendum eros</div>
  <span class="btn-navy">Make Appointments</span>
</div>
<div class="abs dots"><span class="on"></span><span></span><span></span><span></span></div>

<section>
  <div class="abs member">
    <div class="abs member-photo" role="img" aria-label="Portrait of the surgeon in a white coat with a stethoscope"></div>
    <div class="abs member-title">Member</div>
    <div class="abs member-sub">ships</div>
    <div class="abs member-cta">Click Here</div>
  </div>
  <h1 class="abs welcome-h">Welcome To Colin Dwyer</h1>
  <p class="abs welcome-p">Lorem ipsum dolor sit amet, consectetur adipisc ng elit. Proin ultricies vestibulum velit, bibendum condimentum metus faucibus sed. Lorem ipsum dolor sit amet, consectetur adipisc ng elit. Proin ultricies vestibulum velit, bibendum condimentum metus faucibus sed. Lorem ipsum dolor sit amet, consectetur adipisc ng elit. Proin ultricies vestibulum velit, bibendum condimentum metus faucibus sed. Lorem ipsum dolor sit amet, consectetur adipisc ng elit. Proin ultricies vestibulum velit, bibendum condimentum metus faucibus sed. Lorem ipsum dolor sit amet, consectetur adipisc ng elit. Proin ultricies vestibulum</p>
  <div class="abs link" style="left:301px;top:497px">Read More</div>
</section>

<section>
  <div class="abs card" style="left:112px">
    <div class="card-img" role="img" aria-label="Photo of a senior doctor with medical team behind" style="background:linear-gradient(#e9eef3,#cfd8e2)"></div>
    <h3>Surgical Fellowships</h3><p>Lorem ipsum dolor sit amet, eiusmod tempor incididunt ut labore</p><span class="arrow"></span>
  </div>
  <div class="abs card" style="left:303px">
    <div class="card-img" role="img" aria-label="Photo of two doctors reviewing a folder" style="background:linear-gradient(#e4e9ee,#b9c9d8)"></div>
    <h3>Training Programs</h3><p>Lorem ipsum dolor sit amet, eiusmod tempor incididunt ut labore</p><span class="arrow"></span>
  </div>
  <div class="abs card" style="left:494px">
    <div class="card-img" role="img" aria-label="Photo of bare feet standing on a wooden floor" style="background:linear-gradient(#eceae8 55%,#d9a98f)"></div>
    <h3>Tailors Bunion Deformity</h3><p>Lorem ipsum dolor sit amet, eiusmod tempor incididunt ut labore</p><span class="arrow"></span>
  </div>
</section>

<section>
  <h2 class="abs updates-h" style="font-weight:400">New Updates</h2>
  <div class="abs updates-line"></div>
  <div class="abs upd-img" style="top:762px;background:linear-gradient(135deg,#f6e3d6,#dc9d78)" role="img" aria-label="Photo of hands massaging a foot"></div>
  <div class="abs upd-title" style="top:758px">Lorem ipsum dolor sit amet</div>
  <p class="abs upd-text" style="top:777px">Lorem ipsum dolor sit amet, conse ctetur adipisicing elit, sed do eius mod tempor incididunt ut labore et dolore magna aliqua. Quisque bibendum eros quis elit Lorem ipsum dolor sit amet, conse ctetur adipisicing elit, sed do eius mod tempor incididunt ut labore et dolore magna aliqua.</p>
  <div class="abs upd-more" style="top:838px">Read More +</div>
  <div class="abs upd-img" style="top:862px;background:linear-gradient(135deg,#f5dcc8,#d98a62)" role="img" aria-label="Photo of a foot sole held in hands"></div>
  <div class="abs upd-title" style="top:858px">Ceiling Track Hoists</div>
  <p class="abs upd-text" style="top:877px">Lorem ipsum dolor sit amet, conse ctetur adipisicing elit, sed do eius mod tempor incididunt ut labore et dolore magna aliqua. Quisque bibendum eros quis elit Lorem ipsum dolor sit amet, conse ctetur adipisicing elit, sed do eius mod tempor incididunt ut labore et dolore magna aliqua.</p>
  <div class="abs upd-more" style="top:938px">Read More +</div>
</section>

<aside>
  <div class="abs appt"><h2>Make Appointments</h2></div>
  <svg class="abs" style="left:587px;top:758px" width="15" height="15" viewBox="0 0 15 15"><rect x="1" y="2.5" width="13" height="11.5" fill="#fff" stroke="var(--navy)" stroke-width="1.3"/><rect x="1" y="2.5" width="13" height="3" fill="var(--navy)"/><line x1="4.5" y1="1" x2="4.5" y2="4" stroke="var(--navy)" stroke-width="1.3"/><line x1="10.5" y1="1" x2="10.5" y2="4" stroke="var(--navy)" stroke-width="1.3"/><text x="7.5" y="12.3" font-size="5.5" text-anchor="middle" fill="var(--navy)" font-family="Open Sans,sans-serif">31</text></svg>
  <div class="abs field" style="top:781px;height:22px">Name</div>
  <div class="abs field" style="top:810px;height:22px">Phone No</div>
  <div class="abs field" style="top:838px;height:22px">E Mail</div>
  <div class="abs field" style="top:866px;height:38px">Your Enquiry...</div>
  <div class="abs btn-orange">Send Enquiry</div>
</aside>

<footer>
  <div class="abs footer"></div>
  <div class="abs f-h" style="left:112px;top:986px">CONTACT US</div>
  <svg class="abs" style="left:112px;top:1014px" width="8" height="11" viewBox="0 0 8 11"><path d="M4 0.5a3.5 3.5 0 0 1 3.5 3.5C7.5 6.5 4 10.5 4 10.5S0.5 6.5 0.5 4A3.5 3.5 0 0 1 4 0.5z" fill="#888"/><circle cx="4" cy="4" r="1.3" fill="var(--footer)"/></svg>
  <div class="abs f-label" style="left:131px;top:1013px">ADDRESS :</div>
  <div class="abs f-text" style="left:131px;top:1026px;width:105px">Harbourview 42 Seabreeze Parade PO Box 2710, Dunehaven WA 6531</div>
  <div class="abs f-text" style="left:131px;top:1071px;width:105px">Redgum 7 / 18 Pelican Street PO Box 8842, Redgum WA 6432</div>
  <svg class="abs" style="left:263px;top:1013px" width="11" height="11" viewBox="0 0 11 11"><path d="M2 0.5l2 2.5-1 1.5c.8 1.6 1.9 2.7 3.5 3.5l1.5-1 2.5 2-1.5 1.5C5 10.5 0.5 6 0.5 2z" fill="#888"/></svg>
  <div class="abs f-label" style="left:285px;top:1013px">TELEPHONE:</div>
  <div class="abs f-text" style="left:285px;top:1026px">08 9412 7730<br>08 9412 7731</div>
  <svg class="abs" style="left:261px;top:1075px" width="13" height="9" viewBox="0 0 13 9"><rect x=".5" y=".5" width="12" height="8" fill="none" stroke="#888"/><path d="M.5 .5L6.5 5 12.5 .5" fill="none" stroke="#888"/></svg>
  <div class="abs f-label" style="left:282px;top:1072px">MAIL :</div>
  <div class="abs f-text" style="left:282px;top:1086px">reception@coastfootclinic.com.au</div>
  <div class="abs f-h" style="left:382px;top:986px">OUR LOCATION</div>
  <div class="abs map" role="img" aria-label="Map showing the practice locations"></div>
  <div class="abs footer-bar"></div>
  <div class="abs f-brand"><svg width="14" height="14"><circle cx="7" cy="7" r="6" fill="#fff"/></svg><span>Mr Colin Dwyer</span></div>
  <div class="abs copy">©2013 - 2014 Colin Dwyer. Rights Reserved.</div>
</footer>

</body>
</html>
```